Lumaform website scandinavian interior design

Existing website: http://lumaform-example.no/

Webdesign for interior designer Ragna Tvedtholm. The company name is Lumaform. Scandinavian interiør is known to be simple and elegant. The website will be in Norwegian, we are working on the text. The website needs to have a few more pages than just the front page. Here are the different titles of the pages:

1. Hjem
2. Om Lumaform
3. Tjenester og priser
4.. Kontakt oss

There should be Facebook and Instagram icons somewhere at the bottom of the website.

The logo we want to use is attached (pink with black print, see attachment )

We have attached images for inspiration. We want to use some of these colors. The color in the logo, The style should be elegant, modern and delicate.

It is imprtant that the website is user friendly.

Target Market(s)

People who want to decorate their home
Companies and public sector who need to redecorate

Industry/Entity Type

Interior Designer

Coding

Coded - Design and coding required

Number of Pages Required

5+ page

Font styles to use
Other font styles liked:
• see example in the logo breakdown

Requirements
Must have
• Elegant, modern and delicate design
Images of design, see examples attached
Colors similar to the pictures
Should not have
• Too bright colors
Pictures of people

```html
<!DOCTYPE html>
<html lang="no">
<head>
<meta charset="utf-8">
<title>Lumaform – interiør og design</title>
<link href="https://fonts.googleapis.com/css2?family=Playfair+Display:wght@400;500&family=Josefin+Sans:wght@300;400&family=Lato:wght@300;400&display=swap" rel="stylesheet">
<style>
:root{
  --blush:#dcc9c1;
  --mauve:#9b6b68;
  --ink:#3b3633;
  --text:#5c5653;
  --line:#b7aaa5;
  --button:#8f8b85;
  --sage:#a2a69f;
  --sage-line:#c9ccc6;
  --footer-logo:#dfe1dc;
  --white:#ffffff;
}
*{box-sizing:border-box;margin:0;padding:0}
html,body{width:1200px;height:2844px;overflow:hidden;background:var(--white)}
body{position:relative;font-family:"Lato",sans-serif;color:var(--text)}
.abs{position:absolute}

/* header */
.nav-link{position:absolute;top:92px;font-family:"Josefin Sans",sans-serif;font-size:15px;letter-spacing:1.5px;color:var(--ink);padding-bottom:12px;border-bottom:1px solid var(--ink)}
.brand{position:absolute;left:480px;top:44px;width:240px;text-align:center}
.brand-name{font-family:"Playfair Display",serif;font-size:38px;color:var(--ink);display:inline-flex;align-items:center;gap:10px}
.brand-name .dot{width:12px;height:12px;border-radius:50%;background:var(--mauve)}
.brand-tag{font-family:"Josefin Sans",sans-serif;font-size:10px;letter-spacing:2px;color:var(--ink);margin-top:6px}

/* hero */
.hero-band{left:0;top:200px;width:1200px;height:780px;background:var(--blush)}
.hero-card{left:120px;top:320px;width:980px;height:640px;background:var(--white)}
.hero-frame{left:150px;top:350px;width:400px;height:570px;border:1px solid var(--line)}
.hero-title{left:180px;top:395px;width:300px;font-family:"Playfair Display",serif;font-weight:500;font-size:32px;line-height:1.25;color:var(--mauve)}
.hero-text{left:180px;top:580px;width:320px;font-size:14px;line-height:1.6}
.btn{left:180px;top:800px;width:166px;height:46px;background:var(--button);color:var(--white);font-family:"Josefin Sans",sans-serif;font-size:13px;display:flex;align-items:center;justify-content:center;letter-spacing:1px}
.hero-photo{left:600px;top:320px;width:500px;height:620px;background:linear-gradient(160deg,#f4f1ec 0%,#e6ddd1 45%,#b59672 75%,#6f5a44 100%)}

/* feature blocks */
.box{border:1px solid var(--line)}
.h-caps{font-family:"Playfair Display",serif;font-size:26px;letter-spacing:1px;color:var(--ink)}
.body-sm{font-size:14px;line-height:1.6}

/* footer */
.footer{left:0;top:2240px;width:1200px;height:604px;background:var(--sage);color:var(--white)}
.footer-frame{left:120px;top:40px;width:960px;height:440px;border:1px solid var(--sage-line)}
.footer-head{font-family:"Josefin Sans",sans-serif;font-size:15px;letter-spacing:1.5px;font-weight:400}
.footer-small{font-size:12px;line-height:1.7}
</style>
</head>
<body>

<header>
  <a class="nav-link" style="left:100px">HJEM</a>
  <a class="nav-link" style="left:262px">OM LUMAFORM</a>
  <div class="brand">
    <div class="brand-name"><span class="dot"></span>Lumaform</div>
    <div class="brand-tag">FARGE &amp; INTERIØRDESIGN</div>
  </div>
  <a class="nav-link" style="left:722px">TJENESTER OG PRISER</a>
  <a class="nav-link" style="left:995px">KONTAKT OSS</a>
</header>

<section>
  <div class="abs hero-band"></div>
  <div class="abs hero-card"></div>
  <div class="abs hero-photo" role="img" aria-label="Lys skandinavisk spisestue med rundt bord, stoler og grønne planter"></div>
  <div class="abs hero-frame"></div>
  <h1 class="abs hero-title">Trenger du hjelp til utvikling av interiørmiljøer?</h1>
  <p class="abs hero-text">For å finne de optimale løsningene til et prosjekt, enten det er et rom eller flere, trenger man fagkunnskap og kunnskap i markedet. Bruk en planlegger med erfaring og sans for helhet. Vi tilpasser løsninger til boliger, kontorer og offentlige rom – vi finner de beste løsningene for deg og dine.</p>
  <div class="abs btn">Les mer</div>
</section>

<section>
  <div class="abs box" style="left:262px;top:1048px;width:938px;height:204px"></div>
  <div class="abs" style="left:100px;top:1100px;width:500px;height:320px;background:linear-gradient(135deg,#f2efea,#d8cfc3 50%,#7d6d5e)" role="img" aria-label="Lyst rom med stige, hylle og planter ved vinduet"></div>
  <h2 class="abs h-caps" style="left:640px;top:1098px">EKSTERIØR / INTERIØR</h2>
  <p class="abs body-sm" style="left:640px;top:1150px;width:500px">Lumaform hjelper deg med bevisst bruk av materialer i forhold til funksjon, design, fasteiffer, pris m.m.</p>

  <div class="abs box" style="left:40px;top:1480px;width:560px;height:200px"></div>
  <h2 class="abs h-caps" style="left:100px;top:1512px">FORM OG UTTRYKK</h2>
  <p class="abs body-sm" style="left:100px;top:1560px;width:470px">I samarbeid med oppdragsgiver fastsettes det på et tidlig stadie hvilket uttrykk man ønsker for rommet, som en del av forutsetningene for bedriften og prosjektet.</p>
  <div class="abs" style="left:260px;top:1680px;width:340px;height:420px;background:linear-gradient(160deg,#eeeae5,#6c6460 55%,#2f2a28)" role="img" aria-label="Moderne kjøkken med mørk benkeplate og barkrakker"></div>

  <div class="abs" style="left:640px;top:1320px;width:560px;height:540px;background:linear-gradient(150deg,#f5f3ef,#d9d3cb 45%,#a48a6b 80%,#6e5b47)" role="img" aria-label="Lyst kjøkken og spiseplass med grå stoler og oransje detaljer"></div>
  <div class="abs box" style="left:640px;top:1860px;width:560px;height:240px;border-top:none"></div>
  <h2 class="abs h-caps" style="left:1123px;top:1885px">LYS</h2>
  <p class="abs body-sm" style="left:680px;top:1940px;width:490px;text-align:right">Belysning må fungere med funksjonskrav og bør være bevisst handlinger. Det å få riktig belysning i forhold til behov har stor arbeidsmiljø og trivsel å gjøre, og er viktig i forhold til funksjon og design.</p>
</section>

<footer class="abs footer">
  <div class="abs footer-frame"></div>
  <div class="abs" style="left:150px;top:110px;width:220px;text-align:center;color:var(--footer-logo)">
    <div style="font-family:'Playfair Display',serif;font-size:34px;display:inline-flex;align-items:center;gap:10px"><span style="width:11px;height:11px;border-radius:50%;background:var(--footer-logo)"></span>Lumaform</div>
    <div style="font-family:'Josefin Sans',sans-serif;font-size:9px;letter-spacing:2px;margin-top:4px">FARGE &amp; INTERIØRDESIGN</div>
  </div>
  <p class="abs" style="left:142px;top:270px;width:300px;font-size:13px;line-height:1.6">Lumaform AS jobber med utvikling av interiørmiljøer for private, bedrifter og offentlige institusjoner.</p>

  <h3 class="abs footer-head" style="left:600px;top:80px">MENY</h3>
  <ul class="abs" style="left:600px;top:112px;list-style:none;font-size:13px;line-height:1.6">
    <li>Hjem</li><li>Om Lumaform</li><li>Tjenester og priser</li><li>Kontakt oss</li>
  </ul>

  <h3 class="abs footer-head" style="left:852px;top:80px">FØLG OSS</h3>
  <div class="abs" style="left:852px;top:116px;display:flex;gap:18px">
    <span style="width:16px;height:16px;border:1.5px solid var(--white)"></span>
    <span style="width:16px;height:16px;border:1.5px solid var(--white);border-radius:50%"></span>
  </div>

  <h3 class="abs footer-head" style="left:600px;top:272px">KONTAKT OSS</h3>
  <div class="abs footer-small" style="left:600px;top:305px">
    <strong style="font-weight:400;display:block">Adresse</strong>
    Lumaform AS<br>Lindeveien 12<br>3430 Solbakk
  </div>
  <div class="abs footer-small" style="left:852px;top:305px;line-height:1.9">
    <div>Telefon: &nbsp;+47 400 12 345</div>
    <div>Epost: &nbsp;post@lumaform-example.no</div>
    <div>Website: &nbsp;www.lumaform-example.no</div>
  </div>
</footer>

</body>
</html>
```